Local fast-growing company in the service sector

We are looking for a modern business card design, which should also appear on our letterheads

Target Market(s)

Private and industrial sectors

Contact Information for Business Card

Vorname Name
Lindkofer Str. 18
71468 Waiblingen
Tel.: 07163-418259-0
Name@kovaltec-pbz.de

Colors
9d9d9d
919191
aaaaaa

Requirements
Must have
• The logo (file) in silver

```html
<!DOCTYPE html>
<html lang="de">
<head>
<meta charset="utf-8">
<title>Kovaltec PBZ – Visitenkarte</title>
<link href="https://fonts.googleapis.com/css2?family=Roboto:wght@400;500&family=Roboto+Condensed:wght@500;700&display=swap" rel="stylesheet">
<style>
  :root {
    --bg: #e4e2df;
    --card-dark: #1b1c1e;
    --card-light: #f4f4f3;
    --silver: #aaaaaa;
    --silver-mid: #9d9d9d;
    --grey-name: #919191;
    --text: #555555;
    --url-light: #e6e6e6;
  }
  * { margin: 0; padding: 0; box-sizing: border-box; }
  html, body { width: 1200px; height: 960px; overflow: hidden; }
  body {
    position: relative;
    background: var(--bg);
    font-family: "Roboto", Arial, sans-serif;
  }

  .card {
    position: absolute;
    border-radius: 18px;
    box-shadow: 0 6px 14px rgba(0,0,0,0.18);
  }

  /* Back side */
  .card--back {
    left: 320px; top: 102px;
    width: 610px; height: 352px;
    background: var(--card-dark);
  }
  .brand-mark {
    position: absolute;
    left: 0; right: 0; top: 150px;
    display: flex; align-items: center; justify-content: center; gap: 14px;
  }
  .brand-mark__square {
    width: 30px; height: 30px;
    background: var(--silver);
  }
  .brand-mark__name {
    font-family: "Roboto Condensed", "Arial Narrow", sans-serif;
    font-weight: 700;
    font-size: 46px;
    line-height: 1;
    color: var(--silver);
    letter-spacing: 1px;
  }
  .back-url {
    position: absolute;
    left: 0; right: 0; top: 292px;
    text-align: center;
    font-size: 15px;
    letter-spacing: 6.5px;
    color: var(--url-light);
  }

  /* Front side */
  .card--front {
    left: 320px; top: 492px;
    width: 598px; height: 343px;
    background: var(--card-light);
  }
  .front-brand {
    position: absolute;
    right: 32px; top: 50px;
    display: flex; align-items: center; gap: 10px;
  }
  .front-brand__square {
    width: 20px; height: 20px;
    background: var(--silver-mid);
  }
  .front-brand__name {
    font-family: "Roboto Condensed", "Arial Narrow", sans-serif;
    font-weight: 700;
    font-size: 34px;
    line-height: 1;
    color: var(--silver-mid);
  }

  .contact {
    position: absolute;
    left: 30px; top: 174px;
    color: var(--text);
  }
  .contact__name {
    font-family: "Roboto Condensed", "Arial Narrow", sans-serif;
    font-weight: 500;
    font-size: 22px;
    color: var(--grey-name);
    margin-bottom: 8px;
    letter-spacing: 0.2px;
  }
  .contact__address {
    font-size: 14px;
    line-height: 18px;
    margin-bottom: 11px;
  }
  .contact__list { list-style: none; }
  .contact__item {
    display: flex; align-items: center; gap: 8px;
    font-size: 14px; line-height: 19px;
  }
  .contact__icon { width: 14px; height: 14px; fill: #666666; flex: none; }
</style>
</head>
<body>

  <section class="card card--back" aria-label="Kartenrückseite">
    <div class="brand-mark">
      <span class="brand-mark__square"></span>
      <span class="brand-mark__name">KOVALTEC PBZ</span>
    </div>
    <p class="back-url">www.kovaltec-pbz.de</p>
  </section>

  <section class="card card--front" aria-label="Kartenvorderseite">
    <div class="front-brand">
      <span class="front-brand__square"></span>
      <span class="front-brand__name">KOVALTEC PBZ</span>
    </div>

    <div class="contact">
      <h1 class="contact__name">JONAS KELLER</h1>
      <p class="contact__address">Lindkofer Str. 18<br>71468 Waiblingen</p>
      <ul class="contact__list">
        <li class="contact__item">
          <svg class="contact__icon" viewBox="0 0 16 16" aria-hidden="true"><path d="M3.6 1.2l2.3 2.6-1.2 2a9 9 0 0 0 5.5 5.5l2-1.2 2.6 2.3-1.4 2.2C7.8 14.8 1.2 8.2 1.4 2.6z"/></svg>
          <span>07163-418259-0</span>
        </li>
        <li class="contact__item">
          <svg class="contact__icon" viewBox="0 0 16 16" aria-hidden="true"><path d="M1 3.5h14v9H1z M1.8 4.2L8 8.8l6.2-4.6" fill="#666" stroke="#f4f4f3" stroke-width="1"/></svg>
          <span>jonas@kovaltec-pbz.de</span>
        </li>
        <li class="contact__item">
          <svg class="contact__icon" viewBox="0 0 16 16" aria-hidden="true"><circle cx="8" cy="8" r="6.8"/><path d="M4.5 4.5c1.5.5 2 1.8 1.2 3-.6 1 .5 2 1.4 2.3.4 1.3-.4 2.6 0 3.6M10 2.4c-.6 1.4.6 2.3 1.8 2.2.8 1.2-.3 2.6.4 3.4" stroke="#f4f4f3" stroke-width="1.1" fill="none"/></svg>
          <span>www.kovaltec-pbz.de</span>
        </li>
      </ul>
    </div>
  </section>

</body>
</html>
```